Lanterne architecture business cards

We are a new company based in New Zealand. We Specialize in High end Luxury Residential Architecture.

Every home is bespoke and is designed to each clients individual requirements and needs.

I like to design buildings that inspire people through light and form while offering a high level of comfort and usability.

Lines of sight, proportion and balance are fundamental to the spaces I create.
Updates

August 5th is current deadline - Today's date is the 13th of August.

Target Market(s)

New Zealanders who want a custom individual home design, typically 30-65 year old males and females

Industry/Entity Type

Architecture

Contact Information for Business Card

Director - Derek Tolson
Contact Number - 0279164073
Email - info@lanternearchitecture-example.co.nz
Webstie - www.lanternearchitecture-example.co.nz
Social Media - @lanternearchitecture

Font styles to use
Sans Serif

Requirements
Must have
• Logo (Both Sides)
Website
Email
Contact Number
Social Media

Nice to have
• Texture
Should not have
• More than 3 colours - typically I would've thought 2 would be good to match the logo.

```html
<!DOCTYPE html>
<html lang="en">
<head>
<meta charset="utf-8">
<title>Lanterne Architecture — Business Cards</title>
<link rel="stylesheet" href="https://fonts.googleapis.com/css2?family=Poppins:wght@300;400;600&display=swap">
<style>
  :root {
    --page-bg: #d6d6d6;
    --card-ink: #2c2c2c;
    --card-ink-light: #383838;
    --text-light: #f2f2f2;
    --text-soft: #cfcfcf;
  }
  * { margin: 0; padding: 0; box-sizing: border-box; }
  html, body {
    width: 901px;
    height: 1200px;
    overflow: hidden;
    background: var(--page-bg);
    font-family: "Poppins", sans-serif;
    color: var(--text-light);
  }
  .sheet { position: relative; width: 901px; height: 1200px; }
  .card {
    position: absolute;
    left: 100px;
    width: 700px;
    height: 400px;
  }
  .card--front { top: 110px; }
  .card--back { top: 690px; }
  .card-shape { position: absolute; inset: 0; width: 700px; height: 400px; }

  /* brand name block */
  .brand { position: absolute; text-transform: uppercase; font-weight: 300; color: var(--text-light); }
  .brand-mark { display: block; border: 2px solid var(--text-light); border-radius: 50%; }
  .brand-line { display: block; }

  .card--front .brand { left: 56px; top: 140px; }
  .card--front .brand-mark { width: 32px; height: 32px; margin: 0 0 14px 40px; }
  .card--front .brand-line { font-size: 14px; letter-spacing: 6px; line-height: 22px; }

  .card--back .brand { left: 0; right: 0; top: 110px; text-align: center; }
  .card--back .brand-mark { width: 56px; height: 56px; margin: 0 auto 22px; }
  .card--back .brand-line { font-size: 24px; letter-spacing: 12px; line-height: 36px; padding-left: 12px; }

  /* contact block */
  .contact {
    position: absolute;
    right: 50px;
    top: 62px;
    text-align: right;
    text-transform: uppercase;
  }
  .contact-name { font-size: 26px; font-weight: 600; letter-spacing: 0.5px; line-height: 1.1; }
  .contact-role { font-size: 13px; font-weight: 300; letter-spacing: 1.5px; color: var(--text-soft); margin-top: 4px; }
  .contact-rule { width: 210px; height: 2px; background: var(--text-light); margin: 14px 0 18px auto; }
  .contact-line { font-size: 12px; font-weight: 300; letter-spacing: 1.2px; line-height: 20px; }
  .contact-gap { height: 14px; }
  .contact-label { font-size: 10px; font-weight: 600; letter-spacing: 1.5px; color: var(--text-soft); line-height: 18px; }
</style>
</head>
<body>
<main class="sheet">

  <section class="card card--front" aria-label="Business card front">
    <svg class="card-shape" viewBox="0 0 700 400" aria-hidden="true">
      <defs>
        <linearGradient id="card-tone-front" x1="0" y1="0" x2="1" y2="1">
          <stop offset="0" stop-color="var(--card-ink)"/>
          <stop offset="1" stop-color="var(--card-ink-light)"/>
        </linearGradient>
      </defs>
      <path d="M22,0 H200 L230,36 H400 L430,0 H678 Q700,0 700,22 V378 Q700,400 678,400 H560 L530,364 H360 L330,400 H22 Q0,400 0,378 V22 Q0,0 22,0 Z" fill="url(#card-tone-front)"/>
    </svg>

    <div class="brand">
      <span class="brand-mark"></span>
      <span class="brand-line">Lanterne</span>
      <span class="brand-line">Architecture</span>
    </div>

    <div class="contact">
      <p class="contact-name">Derek Tolson</p>
      <p class="contact-role">Director</p>
      <div class="contact-rule"></div>
      <p class="contact-line">0279164073</p>
      <p class="contact-line">info@lanternearchitecture-example.co.nz</p>
      <p class="contact-line">www.lanternearchitecture-example.co.nz</p>
      <div class="contact-gap"></div>
      <p class="contact-label">Social media:</p>
      <p class="contact-line">@lanternearchitecture</p>
    </div>
  </section>

  <section class="card card--back" aria-label="Business card back">
    <svg class="card-shape" viewBox="0 0 700 400" aria-hidden="true">
      <defs>
        <linearGradient id="card-tone-back" x1="0" y1="0" x2="1" y2="1">
          <stop offset="0" stop-color="var(--card-ink)"/>
          <stop offset="1" stop-color="var(--card-ink-light)"/>
        </linearGradient>
      </defs>
      <path d="M22,0 H200 L230,36 H400 L430,0 H678 Q700,0 700,22 V378 Q700,400 678,400 H560 L530,364 H360 L330,400 H22 Q0,400 0,378 V22 Q0,0 22,0 Z" fill="url(#card-tone-back)"/>
    </svg>

    <div class="brand">
      <span class="brand-mark"></span>
      <span class="brand-line">Lanterne</span>
      <span class="brand-line">Architecture</span>
    </div>
  </section>

</main>
</body>
</html>
```